Bref créative |
Business Cards for hardscaping company | ||
Brennock Stoneworks LLC | ||
Use same font as used in my logo | ||
Cutting-Edge Corporate Traditional Modern Professional Simple Bright & Fun-filled |
Dwight Halvorsen | ||
Owner | ||
412 Tollivar Mill Road Ashcombe Ridge, OH 43117 |
brennockstoneworks@quillmarsh.com | ||
Please add the line (all phases of hardscape construction & Snow Removal) | ||

```html
<!DOCTYPE html>
<html lang="en">
<head>
<meta charset="utf-8">
<title>Brennock Stoneworks LLC – Business Card</title>
<link rel="stylesheet" href="https://fonts.googleapis.com/css2?family=Open+Sans:ital,wght@0,400;0,600;1,400;1,700&display=swap">
<style>
  :root {
    --backdrop: #3a3a3a;
    --card: #ffffff;
    --brand-blue: #5b8fd8;
    --band-blue: #5c93f7;
    --block-black: #1a1414;
    --text-grey: #4a4a4a;
  }
  * { margin: 0; padding: 0; box-sizing: border-box; }
  html, body { width: 1200px; height: 915px; overflow: hidden; }
  body {
    background: var(--backdrop);
    font-family: "Open Sans", Arial, sans-serif;
    position: relative;
  }
  .card {
    position: absolute;
    left: 148px; top: 168px;
    width: 869px; height: 495px;
    background: var(--card);
  }
  .wordmark {
    position: absolute;
    left: 0; right: 0; top: 92px;
    text-align: center;
    color: var(--brand-blue);
    font-weight: 400;
    font-size: 52px;
    line-height: 1.15;
    letter-spacing: 2px;
    text-transform: uppercase;
  }
  .tagline {
    position: absolute;
    left: 0; right: 0; top: 280px;
    text-align: center;
    color: var(--brand-blue);
    font-style: italic;
    font-size: 24px;
  }
  .name-block {
    position: absolute;
    left: 0; top: 347px;
    width: 50px; height: 47px;
    background: var(--block-black);
  }
  .name-band {
    position: absolute;
    left: 62px; top: 347px;
    width: 807px; height: 47px;
    background: var(--band-blue);
    color: #fff;
    display: flex; align-items: center;
    padding-left: 255px;
    font-size: 27px;
  }
  .name-band .person { font-weight: 700; font-style: italic; }
  .name-band .role { font-size: 23px; margin-left: 8px; }
  .contact {
    position: absolute;
    left: 0; right: 0; top: 410px;
    display: flex; justify-content: center; align-items: center;
    gap: 20px;
    color: var(--text-grey);
    font-size: 22px;
  }
  .contact-item { display: flex; align-items: center; gap: 10px; }
  .contact-icon { width: 20px; height: 20px; }
  .address {
    position: absolute;
    left: 0; right: 0; top: 450px;
    text-align: center;
    color: var(--text-grey);
    font-size: 22px;
  }
</style>
</head>
<body>
  <div class="card">
    <div class="wordmark">Brennock Stoneworks<br>LLC</div>
    <p class="tagline">all phases of hardscape construction &amp; Snow Removal</p>
    <div class="name-block"></div>
    <div class="name-band"><span class="person">Dwight Halvorsen,</span><span class="role">Owner</span></div>
    <div class="contact">
      <span class="contact-item">
        <svg class="contact-icon" viewBox="0 0 24 24" aria-hidden="true"><path fill="#5b8fd8" d="M6.6 10.8a15.1 15.1 0 0 0 6.6 6.6l2.2-2.2c.3-.3.7-.4 1-.2 1.1.4 2.3.6 3.6.6.6 0 1 .4 1 1V20c0 .6-.4 1-1 1A17 17 0 0 1 3 4c0-.6.4-1 1-1h3.5c.6 0 1 .4 1 1 0 1.3.2 2.5.6 3.6.1.3 0 .7-.2 1z"/></svg>
        610-555-0182
      </span>
      <span class="contact-item">
        <svg class="contact-icon" viewBox="0 0 24 24" aria-hidden="true"><rect x="2" y="5" width="20" height="14" rx="2" fill="#5b8fd8"/><path d="M3 6l9 7 9-7" fill="none" stroke="#fff" stroke-width="1.8"/></svg>
        brennockstoneworks@quillmarsh.com
      </span>
    </div>
    <p class="address">412 Tollivar Mill Road, Ashcombe Ridge, OH 43117</p>
  </div>
</body>
</html>
```